An update to our current wine label

we want to freshen up our current wine label. we have changed it already into a wrap label that is one piece, but we need something that pops a little more. the logo is a bit plain and we plan on raised peinting the Wine stain part of the logo. i wpuld love to have it be huge covering the label, but i cant lose anybofbthe inportant info written on the label either. so im not sure what to do at this point.

```html
<!DOCTYPE html>
<html lang="en">
<head>
<meta charset="utf-8">
<title>Clear Brook Vineyards – Marian's Red Wrap Label</title>
<link rel="stylesheet" href="https://fonts.googleapis.com/css2?family=Cormorant+Garamond:wght@500;600;700&family=Inter:wght@400&display=swap">
<style>
  :root {
    --sky-top: #a9a9c0;
    --sky-peach: #eeb29b;
    --ridge-mist: #6f7696;
    --ridge-blue: #2f4d72;
    --valley-navy: #15254a;
    --night: #0c0b1f;
    --wine: #7a3336;
    --stain-strong: rgba(128, 62, 72, 0.62);
    --stain-soft: rgba(128, 62, 72, 0.18);
    --stain-clear: rgba(128, 62, 72, 0);
    --ink-light: #f4f1ef;
    --ink-soft: #d8c8c6;
    --rule: #ece6e6;
  }
  html, body {
    margin: 0;
    padding: 0;
    width: 1200px;
    height: 873px;
    overflow: hidden;
    background: #ffffff;
  }
  .label {
    position: relative;
    width: 1200px;
    height: 873px;
    overflow: hidden;
    font-family: "Cormorant Garamond", Georgia, serif;
  }
  .landscape {
    position: absolute;
    inset: 0;
    background: linear-gradient(
      to bottom,
      var(--sky-top) 0%,
      var(--sky-peach) 30%,
      var(--ridge-mist) 38%,
      var(--ridge-blue) 52%,
      var(--valley-navy) 68%,
      var(--night) 82%,
      var(--night) 100%
    );
  }
  .stain-area {
    position: absolute;
    left: 150px;
    top: -90px;
    width: 1010px;
    height: 1010px;
    border-radius: 50%;
    background: radial-gradient(
      circle at 50% 50%,
      var(--stain-clear) 0%,
      var(--stain-clear) 58%,
      var(--stain-soft) 70%,
      var(--stain-strong) 84%,
      var(--stain-soft) 95%,
      var(--stain-clear) 100%
    );
  }

  .brand { margin: 0; font-weight: 700; color: var(--wine); }
  .brand-line {
    position: absolute;
    display: block;
    transform: translateX(-50%);
    line-height: 1;
    white-space: nowrap;
  }
  .brand-line-1 { left: 542px; top: 128px; font-size: 178px; letter-spacing: 1px; }
  .brand-line-2 { left: 589px; top: 284px; font-size: 165px; letter-spacing: 2px; }
  .brand-line-3 { left: 643px; top: 421px; font-size: 115px; letter-spacing: 3px; font-weight: 600; }

  .wine-info {
    position: absolute;
    left: 605px;
    transform: translateX(-50%);
    top: 640px;
    text-align: center;
    color: var(--ink-light);
    font-weight: 500;
    white-space: nowrap;
  }
  .vintage { font-size: 24px; line-height: 30px; }
  .designation { font-size: 25px; line-height: 28px; letter-spacing: 1px; }
  .wine-name { font-size: 52px; line-height: 58px; letter-spacing: 10px; margin: 0; font-weight: 500; }
  .appellation { font-size: 25px; line-height: 28px; letter-spacing: 1px; }

  .info-rule {
    position: absolute;
    left: 157px;
    top: 791px;
    width: 886px;
    height: 6px;
    background: var(--rule);
  }
  .wine-type {
    position: absolute;
    left: 314px;
    top: 812px;
    font-size: 21px;
    color: var(--ink-soft);
  }
  .volume {
    position: absolute;
    right: 278px;
    top: 812px;
    font-size: 21px;
    line-height: 27px;
    text-align: right;
    color: var(--ink-soft);
  }

  .side-copy {
    position: absolute;
    margin: 0;
    font-family: "Inter", Arial, sans-serif;
    font-size: 10.5px;
    line-height: 16px;
    writing-mode: vertical-rl;
  }
  .side-copy-top {
    left: 28px;
    top: 56px;
    height: 222px;
    color: #2b2a3a;
  }
  .side-copy-lower {
    left: 28px;
    top: 487px;
    height: 318px;
    color: var(--ink-soft);
  }
  .side-copy-right {
    left: 1064px;
    top: 494px;
    height: 314px;
    color: var(--ink-soft);
    transform: rotate(180deg);
  }
</style>
</head>
<body>
  <main class="label">
    <div class="landscape" role="img" aria-label="Illustrated mountain landscape at dusk with layered blue ridges, a peach sky and dark pine forest in the foreground"></div>
    <div class="stain-area" role="img" aria-label="Large translucent wine-stain ring with drips, raised-print logo element covering the label"></div>

    <p class="side-copy side-copy-top">Lorem ipsum dolor sit amet, consectetuer adipiscing elit, sed diam nonummy nibh euismod tincidunt ut laoreet dolore magna aliquam erat volutpat. Ut wisi</p>

    <h1 class="brand">
      <span class="brand-line brand-line-1">CLEAR</span>
      <span class="brand-line brand-line-2">BROOK</span>
      <span class="brand-line brand-line-3">VINEYARDS</span>
    </h1>

    <p class="side-copy side-copy-lower">Lorem ipsum dolor sit amet, consectetuer adipiscing elit, sed diam nonummy nibh euismod tincidunt ut laoreet dolore magna aliquam erat volutpat. Ut wisi enim ad minim veniam, quis nostrud exerci tation ullamcorper suscipit lobortis nisl ut aliquip ex ea commodo consequat. Duis autem vel eum iriure dolor in hendrerit in vulputate velit esse molestie consequat,</p>

    <p class="side-copy side-copy-right">Lorem ipsum dolor sit amet, consectetuer adipiscing elit, sed diam nonummy nibh euismod tincidunt ut laoreet dolore magna aliquam erat volutpat. Ut wisi enim ad minim veniam, quis nostrud exerci tation ullamcorper suscipit lobortis nisl ut aliquip ex ea commodo consequat. Duis autem vel eum iriure dolor in</p>

    <section class="wine-info">
      <div class="vintage">2023</div>
      <div class="designation">ESTATE BOTTLED</div>
      <h2 class="wine-name">MARIAN’S RED</h2>
      <div class="appellation">ASHFIELD COUNTY</div>
    </section>

    <div class="info-rule"></div>
    <div class="wine-type">Red Wine</div>
    <div class="volume">13% ALC/VOL.<br>750 ML</div>
  </main>
</body>
</html>
```